Web design for a Senior Home Care company

I want a web design for a home care company called Larkmoor Home Care. What LHC does is send caregivers into people's homes to assist with daily living needs such as companionship, food preparation, cleaning, bathing, using the bathroom, etc. Most of the clients are seniors. The people deciding to use LHC are usually the 50 year old children of these senior citizens. Most visitors to the site will be women searching for this service for their parents.

The call to action is to inspire the website visitors to call us to set up an appointment to meet them in their home. The site design should inspire confidence in Larkmoor Home Care to care for people's needs. We want to show the same attributes that a parent should have. Safety, Security and Loving Care.

Again, the goal of the site is to inspire and make it EASY for visitors to contact us either by phone call or through the website. The first choice is that they call us.

To help you with your ideas, In the attachments I've included different versions of our logo, a site map, examples of photos we might use and very rough draft of the website copy.

Target Market(s)

The customers will mostly be seniors. But, the people who will decide to use the company will the the 50 year old children of those seniors. Also, it is mostly women who are looking for help for their parents.

Industry/Entity Type

It Company

Number of Pages Required

5+ page

Requirements
Nice to have
• I want site visitors to easily be able to contact us with a phone call or through the website. The home page should inspire people to call us.

```html
<!DOCTYPE html>
<html lang="en">
<head>
<meta charset="utf-8">
<title>Larkmoor Home Care</title>
<link href="https://fonts.googleapis.com/css2?family=Oswald:wght@400;500&family=Roboto:ital,wght@0,300;0,400;0,500;1,400&display=swap" rel="stylesheet">
<style>
:root{
  --brand:#3b5ba5;
  --brand-dark:#2f4f97;
  --nav-top:#6a98d6;
  --nav-bottom:#4b79bf;
  --nav-active:#2f56a6;
  --btn-light:#5f93d9;
  --quote:#6493d2;
  --ink:#333;
  --muted:#666;
  --soft:#f0f0f0;
  --footer:#3c5ba4;
  --base:#0c0c0c;
  --white:#fff;
}
*{box-sizing:border-box;margin:0;padding:0}
html,body{width:1200px;height:2230px;overflow:hidden;background:var(--white)}
body{position:relative;font-family:"Roboto",Arial,sans-serif;color:var(--ink)}
h1,h2,h3,h4{font-weight:400}
.abs{position:absolute}
.photo{position:absolute;border:3px solid #fff;box-shadow:0 0 0 1px #cfcfcf}

/* header */
.header{top:0;left:0;width:1200px;height:115px;background:var(--white)}
.brand{left:89px;top:36px;display:flex;align-items:center;gap:12px}
.brand-mark{width:34px;height:34px;background:var(--brand)}
.brand-name{font-size:30px;font-weight:500;color:var(--brand);letter-spacing:.5px}
.header-phone{left:654px;top:47px;font-size:18px;color:#222;display:flex;align-items:center;gap:8px}
.btn-book{left:806px;top:41px;width:168px;height:36px;background:var(--btn-light);color:#fff;font-size:14px;display:flex;align-items:center;justify-content:center;border-radius:2px}
.social{left:988px;top:48px;display:flex;gap:12px}
.social span{width:21px;height:21px;border-radius:3px;background:var(--brand)}

/* nav */
.nav{top:115px;left:0;width:1200px;height:71px;background:linear-gradient(var(--nav-top),var(--nav-bottom));display:flex;padding-left:89px}
.nav a{color:#fff;text-decoration:none;font-size:15px;display:flex;align-items:center;padding:0 24px;height:71px}
.nav a.active{background:var(--nav-active);padding:0 29px}

/* hero */
.hero{top:186px;left:0;width:1200px;height:572px;background:linear-gradient(100deg,#e9e3d8 0%,#d7b59c 35%,#c99f86 55%,#e9dccd 80%,#f4efe9 100%)}
.hero-caption{left:89px;top:507px;width:442px;height:223px;background:rgba(35,35,35,.85);padding:20px 24px}
.hero-title{font-family:"Oswald",Arial,sans-serif;font-size:44px;color:#fff;line-height:1.15;letter-spacing:-.5px;white-space:nowrap}
.hero-sub{font-family:"Oswald",Arial,sans-serif;font-weight:400;font-size:25px;color:#fff;line-height:1.3;margin-top:6px}
.hero-phone{font-size:23px;color:#fff;margin-top:12px;display:flex;align-items:center;gap:12px}
.hero-arrows{left:1047px;top:688px;display:flex;gap:2px}
.hero-arrows span{width:31px;height:39px;background:rgba(60,50,45,.75);display:flex;align-items:center;justify-content:center}

/* welcome */
.welcome-photo{left:89px;top:797px;width:434px;height:263px;background:linear-gradient(120deg,#5f8fb0,#c7d6df 50%,#e8e4df)}
.welcome-title{left:550px;top:808px;font-size:26px;color:#333;letter-spacing:.3px}
.welcome-title em{font-style:normal;color:var(--brand)}
.welcome-text{left:550px;top:855px;width:560px;font-size:12.5px;line-height:22px;color:#555}
.welcome-text p+p{margin-top:12px}
.btn-more{left:550px;top:1019px;width:121px;height:34px;background:var(--brand-dark);color:#fff;font-size:13px;font-weight:500;display:flex;align-items:center;justify-content:center;border-radius:3px}

/* services */
.services{top:1103px;left:0;width:1200px;height:444px;background:var(--soft);border-top:1px solid #e2e2e2}
.section-title{width:1200px;text-align:center;font-size:27px;color:#333}
.section-title em{font-style:normal;color:var(--brand)}
.services-sub{top:1195px;width:1200px;text-align:center;font-size:14px;color:#444}
.service{position:absolute;top:1240px;width:248px}
.service-img{position:relative;width:248px;height:158px;border:4px solid #fff;box-shadow:0 0 0 1px #d5d5d5}
.service h3{font-size:15px;color:#333;margin-top:22px;letter-spacing:.3px}
.service p{font-size:11px;line-height:20px;color:#777;margin-top:6px;text-align:justify}
.service a{display:block;font-size:11px;color:var(--brand);margin-top:4px;text-decoration:none}

/* blog & testimonials */
.block-title{font-size:20px;color:#222;letter-spacing:.3px}
.block-title em{font-style:normal;color:var(--brand)}
.post-img{left:92px;width:179px;height:110px;border:3px solid #fff;box-shadow:0 0 0 1px #ddd}
.post{left:291px;width:360px}
.post h4{font-size:15px;color:#222}
.post .date{font-size:11px;color:var(--brand);margin-top:14px}
.post p{font-size:11.5px;line-height:18px;color:#333;margin-top:10px}
.quote{left:779px;top:1621px;width:333px;height:155px;background:var(--quote);border-radius:3px;padding:28px 26px 0 26px;color:#fff;font-size:12.5px;line-height:24px}
.avatar{left:784px;top:1794px;width:80px;height:80px;border-radius:50%;background:radial-gradient(circle at 50% 40%,#e6c9b5,#8a6b5a)}
.author{left:900px;top:1801px;font-size:15px;font-style:italic;color:#333}
.t-arrows{left:900px;top:1847px;display:flex;gap:4px}
.t-arrows span{width:18px;height:18px;border:1px solid #ccc;display:flex;align-items:center;justify-content:center;background:#fff}

/* footer */
.footer{top:1929px;left:0;width:1200px;height:218px;background:var(--footer);color:#fff}
.f-title{top:1971px;font-size:14px;font-weight:400;color:#fff;letter-spacing:.3px}
.f-links{left:92px;top:2005px;list-style:none;font-size:11.5px;line-height:25px;color:#fff}
.f-links li::before{content:"";display:inline-block;border-left:5px solid #fff;border-top:4px solid transparent;border-bottom:4px solid transparent;margin-right:8px}
.f-about{left:248px;top:2008px;width:278px;font-size:11px;line-height:16.5px;text-align:justify;color:#fff}
.f-contact{left:664px;top:2006px;font-size:11.5px;line-height:20px;color:#fff}
.f-contact p{margin-bottom:8px}
.f-follow{left:923px;top:2004px;font-size:13px;color:#fff}
.f-circles{left:928px;top:2040px;display:flex;gap:14px}
.f-circles span{width:33px;height:33px;border:1px solid #fff;border-radius:50%}
.base{top:2147px;left:0;width:1200px;height:83px;background:var(--base);color:#fff;font-size:12px;display:flex;align-items:center;justify-content:center}
</style>
</head>
<body>

<header class="abs header">
  <div class="abs brand"><span class="brand-mark"></span><span class="brand-name">Larkmoor Home Care</span></div>
  <div class="abs header-phone">
    <svg width="16" height="16" viewBox="0 0 16 16"><rect width="16" height="16" rx="2" fill="#3b5ba5"/><path d="M5 3.5l2 2-1 1.3c.6 1.3 1.6 2.3 2.9 2.9l1.3-1 2 2-1.3 1.6C7.6 12 4 8.4 3.6 4.7z" fill="#fff"/></svg>
    (08) 9412 7300
  </div>
  <div class="abs btn-book">BOOK APPOINTMENT</div>
  <div class="abs social"><span></span><span></span><span></span><span></span></div>
</header>

<nav class="abs nav">
  <a class="active">HOME</a><a>ABOUT US</a><a>SERVICES</a><a>FREE IN-HOME CONSULTATION</a><a>CONTACT US</a><a>NEWS/REVIEWS/FAQ</a><a>CLIENT PORTAL</a>
</nav>

<section class="abs hero" role="img" aria-label="Photo of a smiling young caregiver embracing an elderly woman"></section>
<div class="abs hero-caption">
  <div class="hero-title">LARKMOOR HOME CARE</div>
  <div class="hero-sub">Family-Owned, Service You Can Trust<br>Assisting the Inland Empire.</div>
  <div class="hero-phone">
    <svg width="22" height="22" viewBox="0 0 16 16"><rect width="16" height="16" rx="3" fill="#fff"/><path d="M5 3.5l2 2-1 1.3c.6 1.3 1.6 2.3 2.9 2.9l1.3-1 2 2-1.3 1.6C7.6 12 4 8.4 3.6 4.7z" fill="#2a2a2a"/></svg>
    (08) 9412 7300
  </div>
</div>
<div class="abs hero-arrows">
  <span><svg width="10" height="16"><path d="M8 1L2 8l6 7" stroke="#fff" stroke-width="1.5" fill="none"/></svg></span>
  <span><svg width="10" height="16"><path d="M2 1l6 7-6 7" stroke="#fff" stroke-width="1.5" fill="none"/></svg></span>
</div>

<div class="photo welcome-photo" role="img" aria-label="Photo of a caregiver offering a drink to a senior woman in a wheelchair"></div>
<h1 class="abs welcome-title">WELCOME TO <em>LARKMOOR HOME CARE</em></h1>
<div class="abs welcome-text">
  <p>Lorem Ipsum has been the industry's standard dummy text ever since the 1500s, when an unknown printer took a galley of type and scrambled it to make a type specimen book. It has survived not only five centuries, but also the leap into electronic typesetting, remaining essentially unchanged</p>
  <p>Lorem Ipsum has been the industry's standard dummy text ever since the 1500s, when an unknown printer took a galley of type and scrambled it to make a type specimen book. It has survived not only five centuries, but also the leap into electronic typesetting, remaining essentially unchanged</p>
</div>
<div class="abs btn-more">READ MORE</div>

<section class="abs services"></section>
<h2 class="abs section-title" style="top:1151px">OUR <em>SERVICE</em></h2>
<div class="abs services-sub">Neque porro quisquam est qui dolorem ipsum quia dolor sit amet</div>

<div class="service" style="left:86px">
  <div class="service-img" role="img" aria-label="Photo of a caregiver with a senior woman" style="background:linear-gradient(120deg,#7d8f9c,#d9c3b2)"></div>
  <h3>COMPANIONSHIP</h3>
  <p>Lorem Ipsum has been the industry's standard dummy text ever since the 1500s, when an</p>
  <a>Read More &gt;&gt;</a>
</div>
<div class="service" style="left:345px">
  <div class="service-img" role="img" aria-label="Photo of a caregiver and senior preparing food together" style="background:linear-gradient(120deg,#cfc7bd,#5b4c52 60%,#2d2d33)"></div>
  <h3>FOOD PREPARATION</h3>
  <p>Lorem Ipsum has been the industry's standard dummy text ever since the 1500s, when an</p>
  <a>Read More &gt;&gt;</a>
</div>
<div class="service" style="left:604px">
  <div class="service-img" role="img" aria-label="Photo of a caregiver and senior woman in a garden" style="background:linear-gradient(120deg,#6b7a2e,#b59a5a 50%,#3f6a6a)"></div>
  <h3>CLEANING</h3>
  <p>Lorem Ipsum has been the industry's standard dummy text ever since the 1500s, when an</p>
  <a>Read More &gt;&gt;</a>
</div>
<div class="service" style="left:862px">
  <div class="service-img" role="img" aria-label="Photo of a caregiver helping a senior man" style="background:linear-gradient(120deg,#e9e6ea,#b6a3ac 50%,#3c3a55)"></div>
  <h3>USING THE BATHROOM</h3>
  <p>Lorem Ipsum has been the industry's standard dummy text ever since the 1500s, when an</p>
  <a>Read More &gt;&gt;</a>
</div>

<h2 class="abs block-title" style="left:91px;top:1583px">LATEST <em>BLOG</em></h2>
<div class="abs post-img" style="top:1627px;background:linear-gradient(110deg,#e8e4e2,#cdb4a4 60%,#8a5f4e)" role="img" aria-label="Photo of a caregiver with a senior woman"></div>
<div class="abs post" style="top:1632px">
  <h4>Nemo Enim Ipsam Voluptatem</h4>
  <div class="date">JULY 20, 2016</div>
  <p>Lorem ipsum dolor sit amet, consectetur adipiscing elit, sed do eiusmod tempor incididunt ut labore</p>
</div>
<div class="abs post-img" style="top:1767px;background:linear-gradient(110deg,#7a5b43,#5e8fa8 50%,#ead8c8)" role="img" aria-label="Photo of a caregiver assisting a senior on the stairs"></div>
<div class="abs post" style="top:1774px">
  <h4>Nemo Enim Ipsam Voluptatem</h4>
  <div class="date">JULY 20, 2016</div>
  <p>Lorem ipsum dolor sit amet, consectetur adipiscing elit, sed do eiusmod tempor incididunt ut labore</p>
</div>

<h2 class="abs block-title" style="left:777px;top:1583px">TESTIMONIALS</h2>
<div class="abs quote">
  <svg width="20" height="14" viewBox="0 0 20 14" style="vertical-align:-1px;margin-right:6px"><circle cx="4.5" cy="9" r="4" fill="#fff"/><circle cx="14.5" cy="9" r="4" fill="#fff"/><path d="M1 9C1 4 4 1 7 1M11 9c0-5 3-8 6-8" stroke="#fff" stroke-width="2" fill="none"/></svg>Lorem ipsum dolor sit amet, consectetur adipiscing elit, sed do eiusmod tempor incididunt ut labore et dolore magna aliqua. Ut enim ad minim veniam, quis nostrud exercitation <svg width="20" height="14" viewBox="0 0 20 14" style="vertical-align:-4px;margin-left:10px"><circle cx="5.5" cy="5" r="4" fill="#fff"/><circle cx="15.5" cy="5" r="4" fill="#fff"/><path d="M9 5c0 5-3 8-6 8M19 5c0 5-3 8-6 8" stroke="#fff" stroke-width="2" fill="none"/></svg>
</div>
<div class="abs avatar" role="img" aria-label="Portrait photo of the reviewer"></div>
<div class="abs author">Mara Ellison - Manager</div>
<div class="abs t-arrows">
  <span><svg width="6" height="9"><path d="M5 1L1 4.5 5 8" stroke="#555" fill="none"/></svg></span>
  <span><svg width="6" height="9"><path d="M1 1l4 3.5L1 8" stroke="#555" fill="none"/></svg></span>
</div>

<footer class="abs footer"></footer>
<div class="abs f-title" style="left:92px">LINKS</div>
<ul class="abs f-links"><li>HOME</li><li>TEAM</li><li>CONTACT</li><li>LOGIN</li></ul>
<div class="abs f-title" style="left:248px">LARKMOOR HOME CARE</div>
<div class="abs f-about">Lorem Ipsum has been the industry's standard dummy text ever since the 1500s, when an unknown printer took a galley of type and scrambled it to make a type specimen book. It has survived not only five centuries, but also the leap into electronic typesetting, remaining essentially</div>
<div class="abs f-title" style="left:664px">GET IN TOUCH</div>
<div class="abs f-contact">
  <p>Address : Level 12 58 Harbour Lane<br>Sydney NSW 2000 Australia</p>
  <p>Phone : +61 (2) 8140 3321</p>
  <p>Fax : &nbsp;+61 (2) 8140 3390</p>
  <p>Email : &nbsp;info@larkmoorcare.com</p>
</div>
<div class="abs f-title" style="left:923px">FOLLOW US</div>
<div class="abs f-follow">Connect with our social network</div>
<div class="abs f-circles"><span></span><span></span><span></span></div>
<div class="abs base">Copyright © 2016. All Rights Reserved</div>

</body>
</html>
```